New LLC consulting company needs a business card design

I need a business card design for new company in Alexandria Virginia called TK Verdane Consulting LLC. The company is focused on consulting for defense and national security issues with expertise in nuclear and space topics. I would like to see designs that are simple and I am open to colors except for brown.

Target Market(s)

All businesses that are seeking consulting help

Industry/Entity Type

Consulting

Contact Information for Business Card

Name of company - TK Verdane Consulting LLC; name (Delia Hartwig) President; email: hartwigdl47@mailnest.example; Phone: 555-862-4197

Requirements
Must have
• The details described above
Nice to have
• I'm open to all ideas
Should not have
• No brown

```html
<!DOCTYPE html>
<html lang="en">
<head>
<meta charset="utf-8">
<title>TK Verdane Consulting LLC – Business Card</title>
<link href="https://fonts.googleapis.com/css2?family=Roboto:wght@400;500;700&display=swap" rel="stylesheet">
<style>
  :root {
    --brand-blue: #0055a9;
    --ink: #2b2b2b;
    --paper: #ffffff;
    --backdrop: #1e1e1e;
    --rule: #3a3a3a;
  }
  * { margin: 0; padding: 0; box-sizing: border-box; }
  html, body {
    width: 1200px;
    height: 1059px;
    overflow: hidden;
    background: var(--backdrop);
    font-family: "Roboto", Arial, sans-serif;
  }
  .canvas { position: relative; width: 1200px; height: 1059px; }

  .card {
    position: absolute;
    border-radius: 24px;
    overflow: hidden;
  }
  .card-front {
    left: 247px; top: 93px; width: 710px; height: 404px;
    background: var(--paper);
  }
  .card-back {
    left: 247px; top: 559px; width: 700px; height: 398px;
    background: var(--brand-blue);
  }

  /* Brand block */
  .brand-ring {
    position: absolute;
    border-radius: 50%;
    border-style: solid;
  }
  .brand-name {
    position: absolute;
    font-weight: 500;
    text-align: center;
    text-transform: uppercase;
    line-height: 1;
  }
  .brand-name .brand-primary { display: block; letter-spacing: 1px; }
  .brand-name .brand-secondary { display: block; letter-spacing: 1px; margin-top: 6px; }

  .card-front .brand-ring {
    left: 474px; top: 34px; width: 114px; height: 114px;
    border-width: 6px; border-color: var(--brand-blue);
  }
  .card-front .brand-name {
    left: 410px; top: 163px; width: 242px;
    color: var(--brand-blue);
  }
  .card-front .brand-primary { font-size: 36px; }
  .card-front .brand-secondary { font-size: 19px; }

  .card-back .brand-ring {
    left: 283px; top: 67px; width: 136px; height: 136px;
    border-width: 3px; border-color: var(--paper);
  }
  .card-back .brand-name {
    left: 200px; top: 226px; width: 300px;
    color: var(--paper);
  }
  .card-back .brand-primary { font-size: 44px; }
  .card-back .brand-secondary { font-size: 23px; }

  /* Person */
  .person-name {
    position: absolute; left: 38px; top: 250px;
    font-size: 26px; font-weight: 700; color: var(--brand-blue);
  }
  .person-title {
    position: absolute; left: 38px; top: 289px;
    font-size: 18px; font-weight: 400; color: var(--ink);
  }
  .divider {
    position: absolute; left: 40px; top: 325px; width: 613px; height: 1.5px;
    background: var(--rule);
  }

  /* Contacts */
  .contact {
    position: absolute; top: 343px;
    display: flex; align-items: center; gap: 12px;
    font-size: 18px; color: var(--ink); letter-spacing: 0.3px;
  }
  .contact svg { width: 18px; height: 18px; fill: var(--brand-blue); flex: none; }
  .contact-phone { left: 38px; }
  .contact-email { right: 50px; }
</style>
</head>
<body>
<div class="canvas">

  <section class="card card-front" aria-label="Business card front">
    <div class="brand-ring" aria-hidden="true"></div>
    <div class="brand-name">
      <span class="brand-primary">TK Verdane</span>
      <span class="brand-secondary">Consulting LLC</span>
    </div>

    <h1 class="person-name">Delia Hartwig</h1>
    <p class="person-title">President</p>
    <div class="divider"></div>

    <p class="contact contact-phone">
      <svg viewBox="0 0 24 24" aria-hidden="true"><path d="M6.6 10.8a15.1 15.1 0 0 0 6.6 6.6l2.2-2.2a1 1 0 0 1 1-.25 11.4 11.4 0 0 0 3.6.57 1 1 0 0 1 1 1V20a1 1 0 0 1-1 1A17 17 0 0 1 3 4a1 1 0 0 1 1-1h3.5a1 1 0 0 1 1 1c0 1.25.2 2.45.57 3.57a1 1 0 0 1-.25 1z"/></svg>
      555-862-4197
    </p>
    <p class="contact contact-email">
      <svg viewBox="0 0 24 24" aria-hidden="true"><path d="M2 5h20v14H2z M3.5 6.5 12 12.5l8.5-6z" fill-rule="evenodd"/></svg>
      hartwigdl47@mailnest.example
    </p>
  </section>

  <section class="card card-back" aria-label="Business card back">
    <div class="brand-ring" aria-hidden="true"></div>
    <div class="brand-name">
      <span class="brand-primary">TK Verdane</span>
      <span class="brand-secondary">Consulting LLC</span>
    </div>
  </section>

</div>
</body>
</html>
```